Brightwave Travel and Tours

Hotel Reservations
Airline Ticketing
Day Tour

My business is a Travel agency. My services are issuing domestic and international tickets. Book room/hotel reservations local/international.
My color preference is apple green/orange/red/blue.
Images of beaches, tickets,luggage.

Industry/Entity Type

Business

```html
<!DOCTYPE html>
<html lang="en">
<head>
<meta charset="utf-8">
<title>Brightwave Travel and Tours – Business Card</title>
<link href="https://fonts.googleapis.com/css2?family=Nunito+Sans:wght@400;600;800&display=swap" rel="stylesheet">
<style>
  :root {
    --orange: #f5a512;
    --teal: #15739b;
    --white: #ffffff;
    --stage: #ece7df;
  }
  * { margin: 0; padding: 0; box-sizing: border-box; }
  html, body { width: 1200px; height: 800px; overflow: hidden; }
  body {
    background: var(--stage);
    font-family: "Nunito Sans", Arial, sans-serif;
    position: relative;
  }
  .card {
    position: absolute;
    top: 120px;
    width: 340px;
    height: 560px;
    overflow: hidden;
    box-shadow: 0 6px 18px rgba(0,0,0,0.18);
  }
  .card-front { left: 220px; background: var(--orange); }
  .card-back  { left: 640px; background: var(--orange); }
  .card-shapes { position: absolute; inset: 0; }

  .brand {
    position: absolute;
    left: 0; right: 0;
    text-align: center;
    color: var(--teal);
    font-weight: 800;
  }
  .brand-dot {
    display: block;
    margin: 0 auto 12px;
    width: 54px; height: 54px;
    border-radius: 50%;
    background: var(--teal);
  }
  .brand-name { font-size: 30px; line-height: 1.05; letter-spacing: 0.5px; }
  .brand-tagline { font-size: 15px; letter-spacing: 1px; text-transform: uppercase; margin-top: 4px; }
  .card-front .brand { top: 190px; }
  .card-back .brand { top: 36px; }
  .card-back .brand-dot { width: 44px; height: 44px; margin-bottom: 10px; }
  .card-back .brand-name { font-size: 24px; }
  .card-back .brand-tagline { font-size: 13px; }

  .holder {
    position: absolute;
    left: 34px; top: 240px;
    color: var(--white);
  }
  .holder-name { font-size: 28px; font-weight: 600; margin-bottom: 14px; }
  .contact-row {
    display: flex; align-items: flex-start; gap: 12px;
    font-size: 13px; line-height: 1.45; margin-bottom: 12px;
  }
  .contact-row svg { flex: none; margin-top: 3px; }

  .services {
    position: absolute;
    left: 0; right: 0; top: 450px;
    text-align: center;
    color: var(--white);
    font-size: 14px;
    line-height: 1.45;
    list-style: none;
  }
</style>
</head>
<body>

  <section class="card card-front" aria-label="Business card front">
    <svg class="card-shapes" viewBox="0 0 340 560" aria-hidden="true">
      <ellipse cx="170" cy="280" rx="215" ry="158" fill="var(--teal)" transform="rotate(-12 170 280)"/>
      <ellipse cx="175" cy="282" rx="200" ry="140" fill="var(--white)" transform="rotate(-12 175 282)"/>
    </svg>
    <div class="brand">
      <span class="brand-dot"></span>
      <div class="brand-name">Brightwave</div>
      <div class="brand-tagline">Travel and Tours</div>
    </div>
  </section>

  <section class="card card-back" aria-label="Business card back">
    <svg class="card-shapes" viewBox="0 0 340 560" aria-hidden="true">
      <path d="M0 210 Q190 212 340 118 L340 430 L0 430 Z" fill="var(--teal)"/>
      <path d="M0 0 H340 V96 Q190 192 0 192 Z" fill="var(--white)"/>
    </svg>
    <div class="brand">
      <span class="brand-dot"></span>
      <div class="brand-name">Brightwave</div>
      <div class="brand-tagline">Travel and Tours</div>
    </div>

    <div class="holder">
      <h1 class="holder-name">Clara Benton</h1>
      <div class="contact-row">
        <svg width="14" height="14" viewBox="0 0 24 24" aria-hidden="true">
          <path fill="var(--white)" d="M6.6 10.8a15.1 15.1 0 0 0 6.6 6.6l2.2-2.2c.3-.3.7-.4 1-.2 1.1.4 2.3.6 3.6.6.6 0 1 .4 1 1V20c0 .6-.4 1-1 1A17 17 0 0 1 3 4c0-.6.4-1 1-1h3.5c.6 0 1 .4 1 1 0 1.3.2 2.5.6 3.6.1.3 0 .7-.2 1z"/>
        </svg>
        <div>Office: 555 210 384<br>Cell: 555 210 397</div>
      </div>
      <div class="contact-row">
        <svg width="14" height="14" viewBox="0 0 24 24" aria-hidden="true" fill="none" stroke="var(--white)" stroke-width="2">
          <circle cx="12" cy="12" r="10"/><path d="M2 12h20M12 2c3 3 3 17 0 20M12 2c-3 3-3 17 0 20"/>
        </svg>
        <div>www.brightwavetrips.com<br>clara@brightwavetrips.com</div>
      </div>
    </div>

    <ul class="services">
      <li>Hotel Reservations</li>
      <li>Airline Ticketing</li>
      <li>Day Tour</li>
    </ul>
  </section>

</body>
</html>
```